Stationery Design Project for Lakemont Kenbu Kai Karate Studio

We Need a Stationery Design for a Karate School Teaching Okinawa Shorin Ryu Karate in Fairhaven, Ohio, U.S.A.

Target Market(s)

Adults Base Western Speaking aged between 25 and 65 yrs, old that handle household budgets

Industry/Entity Type

School

Requirements
Must have
• Name of business: Lakemont Kenbu Kai Karate Studio
Address: Maplecrest Plaza 38214 US Hwy. 61
Fairhaven, Ohio. 33812
Phone # : 407-555-0183
email : Lakemontkenbukaistudio@samplemail.net
Logo - attatched

```html
<!DOCTYPE html>
<html lang="en">
<head>
<meta charset="utf-8">
<title>Lakemont Kenbu Kai Karate Studio – Stationery</title>
<link rel="stylesheet" href="https://fonts.googleapis.com/css2?family=Source+Sans+3:ital,wght@0,400;0,600;0,700;1,400&display=swap">
<style>
  :root {
    --bg: #e8e8e8;
    --paper: #ffffff;
    --ink: #1a1a1a;
    --text: #333333;
    --red: #b0202a;
    --rule: #9a9a9a;
    --faint: #ececec;
    --flap: #f7f7f7;
    --flap-edge: #dddddd;
  }
  * { margin: 0; padding: 0; box-sizing: border-box; }
  html, body { width: 1196px; height: 1200px; overflow: hidden; }
  body {
    position: relative;
    background: var(--bg);
    font-family: "Source Sans 3", Arial, sans-serif;
    color: var(--text);
  }
  .sheet { position: absolute; background: var(--paper); }

  /* Brand lockup (name + plain circle) */
  .brand { position: absolute; text-align: center; color: var(--ink); font-weight: 700; line-height: 1.05; text-transform: uppercase; white-space: nowrap; }
  .brand .dot { display: block; margin: 0 auto 4px; border-radius: 50%; background: var(--red); }

  /* Letterhead */
  .letterhead { left: 98px; top: 151px; width: 638px; height: 901px; }
  .letterhead .brand { left: 0; right: 0; top: 32px; font-size: 15px; }
  .letterhead .brand .dot { width: 34px; height: 34px; }
  .letter-body { position: absolute; left: 75px; top: 150px; width: 488px; font-size: 10.8px; line-height: 14.7px; }
  .letter-body p { text-align: justify; margin-bottom: 14.5px; }
  .letter-body .salutation { margin-bottom: 14px; }
  .sign-off { position: absolute; left: 75px; top: 614px; font-size: 10.8px; line-height: 14.7px; }
  .signature { position: absolute; left: 75px; top: 648px; width: 60px; height: 46px; background: linear-gradient(135deg, #d8d8d8, #f4f4f4); }
  .signatory { position: absolute; left: 75px; top: 730px; font-size: 10.8px; line-height: 15px; }
  .letter-footer { position: absolute; left: 33px; right: 33px; top: 828px; text-align: center; font-size: 9px; line-height: 12.5px; color: var(--ink); }
  .letter-footer .studio { color: var(--red); font-style: italic; }
  .letter-footer hr { border: 0; border-top: 1px solid var(--rule); margin: 3px 0 4px; }

  /* Envelope back */
  .envelope-back { left: 350px; top: 437px; width: 634px; height: 299px; }
  .envelope-back svg { position: absolute; left: 0; top: 0; }
  .envelope-back .brand { left: 0; right: 0; top: 10px; font-size: 7px; }
  .envelope-back .brand .dot { width: 16px; height: 16px; margin-bottom: 2px; }

  /* Envelope front */
  .envelope-front { left: 405px; top: 523px; width: 637px; height: 300px; overflow: hidden; }
  .envelope-front .brand { left: 12px; top: 28px; width: 100px; font-size: 9px; }
  .envelope-front .brand .dot { width: 24px; height: 24px; }
  .envelope-front .watermark { position: absolute; right: 16px; top: 90px; width: 240px; text-align: center; font-size: 30px; font-weight: 700; line-height: 1.05; color: var(--faint); text-transform: uppercase; }
  .return-address { position: absolute; left: 33px; top: 258px; font-size: 8.5px; line-height: 12px; color: var(--ink); }

  /* Business cards */
  .card { position: absolute; width: 272px; height: 152px; }
  .card-front { left: 850px; top: 41px; background: var(--paper); }
  .card-front .brand { left: 26px; top: 30px; width: 90px; font-size: 8.5px; }
  .card-front .brand .dot { width: 22px; height: 22px; }
  .card-details { position: absolute; right: 26px; top: 34px; text-align: right; font-size: 6.5px; line-height: 9px; color: var(--ink); }
  .card-details .name { font-size: 7.5px; }
  .card-details .role { color: var(--red); margin-bottom: 11px; }
  .card-details .address { margin-bottom: 6px; }
  .card-details .icon { display: inline-block; width: 6px; height: 6px; margin-left: 3px; vertical-align: -0.5px; }
  .card-back { left: 848px; top: 250px; background: var(--red); }
  .card-back .brand { left: 0; right: 0; top: 34px; font-size: 12px; }
  .card-back .brand .dot { width: 34px; height: 34px; background: var(--paper); }
</style>
</head>
<body>

  <!-- Letterhead -->
  <section class="sheet letterhead">
    <div class="brand"><span class="dot"></span>Lakemont Kenbu Kai<br>Karate Studio</div>
    <div class="letter-body">
      <p class="salutation">Dear customer,</p>
      <p>Lorem ipsum dolor sit amet, consectetur adipisicing elit, sed do eiusmod tempor incididunt ut labore et dolore magna aliqua. Ut enim ad minim veniam, quis nostrud exercitation ullamco laboris nisi ut aliquip ex ea commodo consequat. Duis aute irure dolor in reprehenderit in voluptate velit esse cillum dolore eu fugiat nulla pariatur. Excepteur sint occaecat cupidatat non proident, sunt in culpa qui officia deserunt mollit anim id est laborum.</p>
      <p>Lorem ipsum dolor sit amet, consectetur adipisicing elit, sed do eiusmod tempor incididunt ut labore et dolore magna aliqua. Ut enim ad minim veniam, quis nostrud exercitation ullamco laboris nisi ut aliquip ex ea commodo consequat. Duis aute irure dolor in reprehenderit in voluptate velit esse cillum dolore eu fugiat nulla pariatur. Excepteur sint occaecat cupidatat non proident, sunt in culpa qui officia deserunt mollit anim id est laborum.</p>
      <p>Lorem ipsum dolor sit amet, consectetur adipisicing elit, sed do eiusmod tempor incididunt ut labore et dolore magna aliqua. Ut enim ad minim veniam, quis nostrud exercitation ullamco laboris nisi ut aliquip ex ea commodo consequat. Duis aute irure dolor in reprehenderit in voluptate velit esse cillum dolore eu fugiat nulla pariatur. Excepteur sint occaecat cupidatat non proident, sunt in culpa qui officia deserunt mollit anim id est laborum.</p>
      <p>Lorem ipsum dolor sit amet, consectetur adipisicing elit, sed do eiusmod tempor incididunt ut labore et dolore magna aliqua. Ut enim ad minim veniam, quis nostrud exercitation ullamco laboris nisi ut aliquip ex ea commodo consequat. Duis aute irure dolor in reprehenderit in voluptate velit esse cillum dolore eu fugiat nulla pariatur. Excepteur sint occaecat cupidatat non proident, sunt in culpa qui officia deserunt mollit anim id est laborum.</p>
      <p>Lorem ipsum dolor sit amet, consectetur adipisicing elit, sed do eiusmod tempor incididunt ut labore et dolore magna aliqua. Ut enim ad minim veniam, quis nostrud exercitation ullamco laboris nisi ut aliquip ex ea commodo consequat. Duis aute irure dolor in reprehenderit in voluptate velit esse cillum dolore eu fugiat nulla pariatur. Excepteur sint occaecat cupidatat non proident, sunt in culpa qui officia deserunt mollit anim id est laborum.</p>
    </div>
    <p class="sign-off">Yours Sincerely,</p>
    <div class="signature" role="img" aria-label="Handwritten signature of the general director"></div>
    <p class="signatory">Daniel Hart<br>General Director</p>
    <footer class="letter-footer">
      <div class="studio">Lakemont Kenbu Kai Karate Studio</div>
      <hr>
      <div>Maplecrest Plaza, 38214 US Hwy. 61, Fairhaven, Ohio. 33812 &nbsp;•&nbsp; 407-555-0183</div>
      <div>Lakemontkenbukaistudio@samplemail.net</div>
    </footer>
  </section>

  <!-- Envelope, back with flap -->
  <section class="sheet envelope-back">
    <svg width="634" height="299" viewBox="0 0 634 299" aria-hidden="true">
      <path d="M0 0 H634 V18 C560 40 420 70 330 78 C322 79 312 79 304 78 C214 70 74 40 0 18 Z" fill="var(--flap)" stroke="var(--flap-edge)" stroke-width="1"/>
    </svg>
    <div class="brand"><span class="dot"></span>Lakemont Kenbu Kai</div>
  </section>

  <!-- Envelope, front -->
  <section class="sheet envelope-front">
    <div class="watermark" aria-hidden="true">Lakemont Kenbu Kai</div>
    <div class="brand"><span class="dot"></span>Lakemont Kenbu Kai<br>Karate Studio</div>
    <p class="return-address">Maplecrest Plaza, 38214 US Hwy. 61<br>Fairhaven, Ohio. 33812</p>
  </section>

  <!-- Business card, details side -->
  <section class="card card-front">
    <div class="brand"><span class="dot"></span>Lakemont Kenbu Kai<br>Karate Studio</div>
    <div class="card-details">
      <div class="name">Sensei Alan R. Moreno</div>
      <div class="role">Instructor</div>
      <div class="address">Maplecrest Plaza<br>38214 US Hwy. 61<br>Fairhaven, Ohio. 33812</div>
      <div>407-555-0183<svg class="icon" viewBox="0 0 10 10" aria-hidden="true"><path d="M2 1 L4 1 L5 3.5 L3.8 4.5 C4.4 5.8 5.2 6.6 6.5 7.2 L7.5 6 L10 7 L10 9 C5 9.5 0.5 5 1 1 Z" fill="var(--red)"/></svg></div>
      <div>Lakemontkenbukaistudio@samplemail.net<svg class="icon" viewBox="0 0 10 10" aria-hidden="true"><rect x="0.5" y="2" width="9" height="6.5" fill="var(--red)"/><path d="M0.5 2 L5 5.8 L9.5 2" fill="none" stroke="#fff" stroke-width="1"/></svg></div>
    </div>
  </section>

  <!-- Business card, brand side -->
  <section class="card card-back">
    <div class="brand"><span class="dot"></span>Lakemont Kenbu Kai<br>Karate Studio</div>
  </section>

</body>
</html>
```